Web Design

We need a new website for our company. We perform several functions:

1 - IT and Network Support
2 - Computer Consultancy
3 - Cloud Services
4 - Hosted Mailvane & Online Backup
5 - Internet Connections & VOIP

Examples of some of the designs we like can be seen on:
• www.brelvox.com
• www.quintaro.com

I urgently need a new website to be designed to enable me to look more professional. My competitors website is www.tdmq.co.uk

I also want to be able to look much more professional, like www.brelvox.com www.quintaro.com

I have attached how I would like the website to look

Task outline
To design a home page and another internal skeleton page for a website following our requirements specification and wireframe layout/structure

Task description
We are looking for a modern, attractive, clean design for our new website to reflect our businesses professionalism and high quality services that we offer.
• www.brelvox.com
• www.quintaro.com
We would like a design for a home page and one other skeleton subpage for our website. We have provided a wireframe image to assist, showing how we would like the layout/structure of our website to follow which also highlights where we would like specific content/features to go.
We have listed what features the site must have in the requirements section.
The final design should communicate to our users that we are a professional business that offer high quality services and that we are a company they can trust and rely on.

Look and feel
The wireframe we have attached is a representation of how we would like the layout and structure of the website to be designed. We would like to have a corporate theme to our website.

Colours
Open to interpretation by the designer, as long as the colours suit a corporate theme and give off a professional look and feel.

Requirements
The design must have the following:

General
• Home page design (Based on attached wireframe).
• Internal Page design (This needs to be a skeleton page which can be used for implemented the content for all over pages).

• Contact details to be visible on every page, contact number at the header and all other relative details in the footer section.
• Social networking icons within the footer section of the site.
• Avoid the use of unprofessional images for buttons, icons and banners etc.
Features desired
• Drop down navigation bar. Please see the attached image for inspiration for its design/layout.
o We would like a similar drop down menu design to the one on this site: www.tdmq.co.uk.
• Image slider at the header of every page just beneath the navigation bar.
o We would like the Plexa slider to be used for the image slider. Please use this link for an example of it in action: http://www.scriptloomhub.net/demo/plexa-slider/
o The image slider needs to be larger on the home page.
o The image slider can be smaller on the rest of the pages of the site.
• Chirply feed present on every page.
• News/Blog feed present on every page.
• Call back form present on every page.
• Wayfindr Map implementation above footer on every page.

A user friendly, accessible design that is easy to use and easy for the user to understand. Must have a corporate theme to reflect the professionalism of our business. Content flows logically and keep content spaced out so that it does not make the site look cluttered.

Target Market(s)

Small to Mid sized Business, Large Banks and Legal, corporate, business - non-technical users

Industry/Entity Type

Business

Font styles to use
Sans Serif

```html
<!DOCTYPE html>
<html lang="en">
<head>
<meta charset="utf-8">
<title>Tidewell Systems – Onsite IT Support</title>
<link href="https://fonts.googleapis.com/css2?family=Open+Sans:wght@400;600;700&display=swap" rel="stylesheet">
<style>
:root{
  --ink:#333;
  --muted:#666;
  --blue:#1f8bcd;
  --blue-dark:#136aa8;
  --orange:#f7890f;
  --green:#6aad3d;
  --page:#f2f1f2;
  --topbar:#1c1c1c;
  --footer:#1f1f1f;
  --footer-base:#121212;
  --line:#dcdcdc;
  --white:#fff;
}
*{box-sizing:border-box;margin:0;padding:0}
html,body{width:692px;height:1200px;overflow:hidden;background:var(--page)}
body{font-family:"Open Sans",Arial,sans-serif;color:var(--ink);font-size:7px}
.page{position:relative;width:692px;height:1200px;overflow:hidden;background:var(--page)}
.abs{position:absolute}

/* top bar */
.topbar{left:0;top:0;width:692px;height:19px;background:var(--topbar)}
.topbar .call{right:92px;top:5px;color:var(--blue);font-size:7.5px}
.topbar .call b{font-weight:700}
.topbar .chat{right:41px;top:4px;height:11px;padding:0 5px;background:var(--green);color:#fff;font-size:6px;line-height:11px;border-radius:2px}

/* header */
.header{left:0;top:19px;width:692px;height:49px;background:var(--white)}
.brand{left:90px;top:15px;display:flex;align-items:center;gap:6px;color:var(--blue);font-size:13px;letter-spacing:.5px}
.brand .mark{width:8px;height:8px;border-radius:50%;background:var(--blue)}
.nav{right:90px;top:21px;display:flex;gap:9px;font-size:8px;color:#555}
.nav a{color:#555;text-decoration:none}
.nav .active{color:var(--blue)}
.nav .sep{color:#888}

/* hero */
.hero{left:0;top:68px;width:692px;height:252px;background:
  linear-gradient(180deg,rgba(242,241,242,0) 0%,rgba(242,241,242,0) 72%,#f2f1f2 100%),
  linear-gradient(90deg,#2c5a86 0%,#5b86b2 40%,#9fc0dc 75%,#c9dcec 100%)}
.hero-copy{left:91px;top:113px;color:#fff}
.hero-copy h1{font-size:22px;font-weight:700;line-height:1.1}
.hero-copy h2{font-size:15.5px;font-weight:400;margin-top:3px}
.hero-copy p{width:262px;font-size:8px;line-height:1.5;margin-top:10px}
.hero-cta{left:91px;top:234px;width:126px;height:24px;background:var(--orange);color:#fff;font-size:10px;text-align:center;line-height:24px;border-radius:2px}
.dots{left:326px;top:311px;display:flex;gap:7px}
.dots i{width:5px;height:5px;border-radius:50%;background:#d3d3d3;display:block}
.dots i.on{background:var(--green)}

/* welcome */
.section-title{font-size:13.5px;font-weight:400;color:#333}
.welcome-title{left:91px;top:355px}
.service{width:180px;height:86px}
.service .icon{left:0;top:0;width:44px;height:44px;border-radius:50%;background:var(--blue);border:3px solid #bfe0f4}
.service .icon svg{position:absolute;left:11px;top:11px}
.service h3{left:51px;top:0;font-size:9px;font-weight:400;color:var(--blue)}
.service p{left:51px;top:14px;width:135px;font-size:6.5px;line-height:13px;color:#444}
.btn-more{left:53px;top:59px;width:75px;height:16px;background:var(--orange);color:#fff;font-size:7.5px;text-align:center;line-height:16px;border-radius:1px}

/* call back */
.callback{left:459px;top:355px;width:143px;height:201px;background:#fff;border:1px solid #e2e2e2}
.callback h3{height:21px;background:var(--blue);color:#fff;font-size:11px;font-weight:400;padding:3px 7px}
.callback .lead{padding:6px 8px 0;font-size:5.8px;line-height:1.45;color:#555}
.field{margin:5px 7px 0;height:18px;border:1px solid #d8d8d8;font-size:6px;color:#777;padding:5px 5px}
.field.msg{height:50px}
.send{margin:8px 0 0 7px;width:97px;height:19px;background:var(--green);color:#fff;font-size:7.5px;text-align:center;line-height:19px;border-radius:1px}

.divider{left:91px;top:574px;width:511px;height:1px;background:var(--line)}

/* testimonials */
.clients-title{left:91px;top:582px}
.quote{width:154px;height:64px;background:#f7f7f7;border:1px solid #e6e6e6;padding:5px 9px}
.quote .who{font-size:5.5px;color:var(--blue);line-height:7px}
.quote .tag{font-size:4.5px;color:#444;line-height:6px}
.quote .bar{width:34px;height:1px;background:#8fc4e6;margin:3px 0 2px}
.quote .body{font-size:4.5px;line-height:8px;color:#777;font-style:italic;padding-left:9px;position:relative}
.quote .body b,.quote .end{color:#8fc4e6;font-size:11px;font-style:normal;font-weight:700;line-height:8px}
.quote .body b{position:absolute;left:0;top:1px}
.quote .end{display:block;margin-left:68px;height:8px}
.avatar{width:19px;height:19px;border-radius:50%;background:linear-gradient(#c9a58a,#8b6a55);border:2px solid #fff;box-shadow:0 0 0 1px #ddd}
.view-all{left:237px;top:771px;width:53px;height:16px;background:var(--orange);color:#fff;font-size:7px;text-align:center;line-height:16px;border-radius:1px}

/* side feeds */
.feed{left:459px;top:587px;width:143px}
.profile{display:flex;gap:6px;align-items:center;padding-bottom:5px;border-bottom:1px solid var(--line)}
.profile .pic{width:26px;height:26px;border:1px solid #ccc;background:#e8eef5;display:flex;align-items:center;justify-content:center}
.profile .pic i{width:14px;height:14px;border-radius:50%;background:var(--blue-dark);display:block}
.profile .name{font-size:7px;color:#555}
.profile .handle{font-size:10.5px;color:#333}
.tweet{font-size:5.8px;line-height:1.5;color:#444;margin-top:4px}
.tweet .hl{color:var(--orange)}
.tweet .meta{color:#999;font-size:5px;margin-top:2px}
.follow{display:flex;justify-content:space-between;align-items:center;margin-top:6px;padding:5px 0;border-top:1px solid var(--line);border-bottom:1px solid var(--line);white-space:nowrap}
.follow .tw{display:flex;align-items:center;gap:4px;font-size:7.5px;color:#2a9fd8;font-weight:600}
.follow .tw i{width:9px;height:9px;border-radius:50%;background:#2a9fd8;display:block}
.follow .join{font-size:6.5px;color:var(--orange);text-decoration:underline}
.news-title{font-size:11.5px;margin-top:9px;color:#333;font-weight:400}
.news-item{display:flex;gap:5px;padding:6px 0;border-bottom:1px solid var(--line)}
.news-item:first-of-type{border-top:1px solid var(--line)}
.news-item .thumb{flex:none;width:28px;height:25px;border:1px solid #ccc;background:linear-gradient(#dfe8f2,#8fa9c4)}
.news-item h4{font-size:6.3px;font-weight:400;color:var(--blue)}
.news-item p{font-size:6px;line-height:1.45;color:#444;margin-top:2px}
.news-item p span{color:var(--orange)}

/* partners */
.partners{left:0;top:807px;width:692px;height:56px;background:#fff;border-top:1px solid #ddd;display:flex;justify-content:center;align-items:center;gap:14px}
.badge{height:26px;background:#d9d9d9;border-radius:2px}
.badge.round{border-radius:50%;width:26px;background:#555}
.badge.dark{background:#6b6b6b}

/* map */
.map{left:0;top:863px;width:692px;height:180px;background:linear-gradient(100deg,#a9c3dd 0%,#b4cbe0 24%,#ddddd0 34%,#ece7d8 55%,#e7e3cf 100%)}
.map-pan{left:93px;top:876px;width:24px;height:24px;border-radius:50%;background:#fff;border:1px solid #bbb}
.map-pan svg{position:absolute;left:4px;top:4px}
.map-zoom{left:101px;top:908px;width:8px;height:114px}
.map-zoom .btn{position:absolute;left:0;width:8px;height:8px;background:#fff;border:1px solid #aaa;font-size:7px;line-height:6px;text-align:center;color:#555}
.map-zoom .track{position:absolute;left:3px;top:22px;width:2px;height:82px;background:#c8c8c8}
.map-type{left:652px;top:866px;width:40px;height:38px;background:#fff;border:1px solid #aaa;font-size:6px;color:#333;text-align:center}
.map-type .thumb{height:22px;background:linear-gradient(#4b6d8c,#6f8f6a)}
.map-type span{display:block;line-height:14px}
.map-traffic{left:652px;top:905px;width:35px;height:16px;background:#fff;border:1px solid #aaa;font-size:6px;color:#333;text-align:center;line-height:14px}

/* footer */
.footer{left:0;top:1043px;width:692px;height:129px;background:var(--footer);color:#ddd}
.footer h5{font-size:10.5px;font-weight:400;color:var(--blue)}
.footer ul{list-style:none;font-size:6px;line-height:12px;margin-top:9px}
.footer .contact ul{line-height:15px}
.social li{display:flex;align-items:center;gap:6px;line-height:18px}
.social i{width:12px;height:12px;border-radius:2px;background:#2f8ed1;display:block}
.base{left:0;top:1172px;width:692px;height:28px;background:var(--footer-base);color:#ddd;font-size:6px}
.base .copy{left:91px;top:10px}
.base .copy span{color:var(--blue)}
.base .legal{right:90px;top:10px}
</style>
</head>
<body>
<div class="page">

  <div class="abs topbar">
    <div class="abs call">Call us : <b>00 987 654 321</b></div>
    <div class="abs chat">Live Chat</div>
  </div>

  <header class="abs header">
    <div class="abs brand"><span class="mark"></span>Tidewell Systems</div>
    <nav class="abs nav">
      <a class="active" href="#">HOME</a><span class="sep">/</span>
      <a href="#">PRODUCTS</a><span class="sep">/</span>
      <a href="#">COMPANY</a><span class="sep">/</span>
      <a href="#">BLOG</a>
    </nav>
  </header>

  <section class="abs hero" role="img" aria-label="Slider photo: smiling IT consultant with a laptop in front of a blurred blue server room, edged by soft white clouds"></section>
  <div class="abs hero-copy">
    <h1>Onsite IT Support</h1>
    <h2>Northgate Certified Experts</h2>
    <p>IT support services are very important to every business in Glasgow and it's surrounding areas. Tidewell Systems LIMITED has been proven to offer the best business solutions, support services, cloud services, and more to businesses across the UK and Scotland.</p>
  </div>
  <div class="abs hero-cta">Get Starte Now</div>
  <div class="abs dots"><i></i><i class="on"></i><i></i><i></i></div>

  <h2 class="abs section-title welcome-title">Welcome To Tidewell Systems</h2>

  <div class="abs service" style="left:91px;top:386px">
    <div class="abs icon"><svg width="16" height="16" viewBox="0 0 16 16"><path d="M4 11a3 3 0 0 1 0-6 4 4 0 0 1 8 1 2.5 2.5 0 0 1 0 5" fill="none" stroke="#fff" stroke-width="1.3"/><path d="M8 7v7M5.5 11.5 8 14l2.5-2.5" fill="none" stroke="#fff" stroke-width="1.3"/></svg></div>
    <h3 class="abs">Online Backup</h3>
    <p class="abs">Protect your valuable data securely offsite.<br>Instant Recovery.<br>Unlimited Data Plans Available.</p>
    <div class="abs btn-more">Find Out More</div>
  </div>
  <div class="abs service" style="left:286px;top:386px">
    <div class="abs icon"><svg width="16" height="16" viewBox="0 0 16 16" fill="#fff"><rect x="6" y="1" width="4" height="3"/><rect x="1" y="11" width="4" height="3"/><rect x="6" y="11" width="4" height="3"/><rect x="11" y="11" width="4" height="3"/><path d="M8 4v7M3 11V8h10v3" fill="none" stroke="#fff"/></svg></div>
    <h3 class="abs">Onsite IT Support</h3>
    <p class="abs">No Travel or Call Out Charge.<br>Northgate and Corvane Engineers 24*7.<br>Fixed Cost Repairs.</p>
    <div class="abs btn-more">Find Out More</div>
  </div>
  <div class="abs service" style="left:91px;top:480px">
    <div class="abs icon"><svg width="16" height="16" viewBox="0 0 16 16"><circle cx="8" cy="5" r="3" fill="none" stroke="#fff" stroke-width="1.3"/><path d="M2 15c1-4 4-5 6-5s5 1 6 5" fill="none" stroke="#fff" stroke-width="1.3"/></svg></div>
    <h3 class="abs">Remote IT Support</h3>
    <p class="abs">Anyplace, Anytime - we fix YOUR issues.<br>Experts on - call 24*7.<br>Fixed Costs.</p>
    <div class="abs btn-more">Find Out More</div>
  </div>
  <div class="abs service" style="left:286px;top:480px">
    <div class="abs icon"><svg width="16" height="16" viewBox="0 0 16 16"><rect x="1.5" y="3.5" width="13" height="9" fill="none" stroke="#fff" stroke-width="1.3"/><path d="M1.5 3.5 8 9l6.5-5.5" fill="none" stroke="#fff" stroke-width="1.3"/></svg></div>
    <h3 class="abs">Hosted Mailvane</h3>
    <p class="abs">Throw out your Email server!<br>Let Us Manage your Email!<br>Plans from $5.95 a month.</p>
    <div class="abs btn-more">Find Out More</div>
  </div>

  <aside class="abs callback">
    <h3>Call Back Form</h3>
    <p class="lead">We guarantee to respond within one hour<br>Alternatively call us on: 0141 555 0192</p>
    <div class="field">Name</div>
    <div class="field">Email</div>
    <div class="field">Phone</div>
    <div class="field msg">Message</div>
    <div class="send">Send Now !</div>
  </aside>

  <div class="abs divider"></div>

  <h2 class="abs section-title clients-title">What Our Clients Say</h2>

  <div class="abs quote" style="left:91px;top:608px">
    <div class="who">Mark Ellison</div><div class="tag">Contrary to popular belief, Lorem Ipsum is not simply</div><div class="bar"></div>
    <div class="body"><b>“</b>Lorem Ipsum is simply dummy text of the printing and type-setting industry. Lorem Ipsum has been the industry's standard dummy text ever since the.</div><span class="end">”</span>
  </div>
  <div class="abs quote" style="left:284px;top:608px">
    <div class="who">Mark Ellison</div><div class="tag">Contrary to popular belief, Lorem Ipsum is not simply</div><div class="bar"></div>
    <div class="body"><b>“</b>Lorem Ipsum is simply dummy text of the printing and type-setting industry. Lorem Ipsum has been the industry's standard dummy text ever since the .</div><span class="end">”</span>
  </div>
  <div class="abs quote" style="left:91px;top:690px">
    <div class="who">Mark Ellison</div><div class="tag">Contrary to popular belief, Lorem Ipsum is not simply</div><div class="bar"></div>
    <div class="body"><b>“</b>Lorem Ipsum is simply dummy text of the printing and type-setting industry. Lorem Ipsum has been the industry's standard dummy text ever since the.</div><span class="end">”</span>
  </div>
  <div class="abs quote" style="left:284px;top:690px">
    <div class="who">Mark Ellison</div><div class="tag">Contrary to popular belief, Lorem Ipsum is not simply</div><div class="bar"></div>
    <div class="body"><b>“</b>Lorem Ipsum is simply dummy text of the printing and type-setting industry. Lorem Ipsum has been the industry's standard dummy text ever since the .</div><span class="end">”</span>
  </div>
  <div class="abs avatar" style="left:255px;top:609px" role="img" aria-label="Client portrait"></div>
  <div class="abs avatar" style="left:255px;top:652px" role="img" aria-label="Client portrait"></div>
  <div class="abs avatar" style="left:255px;top:690px" role="img" aria-label="Client portrait"></div>
  <div class="abs avatar" style="left:255px;top:733px" role="img" aria-label="Client portrait"></div>
  <div class="abs view-all">View All</div>

  <aside class="abs feed">
    <div class="profile">
      <div class="pic"><i></i></div>
      <div><div class="name">Tidewell Systems</div><div class="handle">tidewell_IT</div></div>
    </div>
    <p class="tweet"><span class="hl">tidewell_IT</span> New server going in, new customers in <span class="hl">#glasgow</span> and <span class="hl">#hamilton</span> . Exciting times!
      <span class="meta" style="display:block">3 months . reply . retweet . favorite</span></p>
    <div class="follow"><span class="tw"><i></i>Follow us on Chirply</span><span class="join">join the conversation</span></div>
    <h3 class="news-title">News and Blog</h3>
    <div style="margin-top:5px">
      <div class="news-item"><div class="thumb" role="img" aria-label="Blog thumbnail"></div><div><h4>Why Our Competitors Hate Us....</h4><p>When you hire IT Consultants from us, we give you <span>[...]</span></p></div></div>
      <div class="news-item"><div class="thumb" role="img" aria-label="Blog thumbnail"></div><div><h4>Why consider an IT Audit?</h4><p>Q: Does my company need an IT audit? Will it <span>[...]</span></p></div></div>
    </div>
  </aside>

  <section class="abs partners" aria-label="Partner accreditations">
    <div class="badge dark" style="width:44px"></div>
    <div class="badge" style="width:36px"></div>
    <div class="badge" style="width:34px"></div>
    <div class="badge" style="width:48px"></div>
    <div class="badge" style="width:46px"></div>
    <div class="badge" style="width:26px;height:30px"></div>
    <div class="badge" style="width:46px"></div>
    <div class="badge" style="width:38px;height:30px"></div>
    <div class="badge round" style="width:28px;height:28px"></div>
  </section>

  <section class="abs map" role="img" aria-label="Wayfindr Map of the Netherlands with office markers around Amsterdam"></section>
  <div class="abs map-pan" aria-hidden="true"><svg width="16" height="16" viewBox="0 0 16 16" fill="#777"><path d="M8 1 6 4h4zM8 15l-2-3h4zM1 8l3-2v4zM15 8l-3-2v4z"/></svg></div>
  <div class="abs map-zoom" aria-hidden="true">
    <div class="btn" style="top:0">+</div>
    <div class="btn" style="top:12px">+</div>
    <div class="track"></div>
    <div class="btn" style="top:106px">−</div>
  </div>
  <div class="abs map-type"><div class="thumb"></div><span>Satellite</span></div>
  <div class="abs map-traffic">Traffic</div>

  <footer class="abs footer">
    <div class="abs contact" style="left:91px;top:10px">
      <h5>Contact Information</h5>
      <ul><li>Tidewell Systems Limited</li><li>14-16 Mill Lane, Dalry, KA24 9XQ</li><li>T. +44(0)141 5550192</li><li>hello@tidewell-systems.com</li></ul>
    </div>
    <div class="abs" style="left:245px;top:10px">
      <h5>Navigation</h5>
      <div style="display:flex;gap:35px">
        <ul><li>Home</li><li>Company</li><li>IT Support</li><li>Cloud Services</li><li>Partners</li></ul>
        <ul><li>Contact Us</li><li>News</li><li>Terms &amp; Conditions</li><li>Sitemap</li></ul>
      </div>
    </div>
    <div class="abs" style="left:430px;top:10px">
      <h5>IT Support</h5>
      <ul><li>IT Support Glasgow</li><li>IT Support Edinburgh</li><li>IT Support Perth</li><li>IT Support Stirling</li><li>IT Support Paisley</li></ul>
    </div>
    <div class="abs" style="left:549px;top:10px">
      <h5>Follow Us!</h5>
      <ul class="social"><li><i></i>Friendhub</li><li><i></i>Chirply</li><li><i></i>Linkpro</li></ul>
    </div>
  </footer>

  <div class="abs base">
    <div class="abs copy">Copyright © 2014 <span>TIDEWELL</span>.  All Rights reserved.</div>
    <div class="abs legal">Terms of Condition &amp; Privacy Policy</div>
  </div>

</div>
</body>
</html>
```